Construction company looking for modern

**Tallow Crest Joinery Limited**

We need a website for a renovation/remodeling company based in Hamilton, New Zealand. Ideally it will catch clients' attention and be modern and professional looking. I have attached a logo that I have just recently had made (through PixelHarbor). If the website could reflect this style and colour schemes, that would be awesome. The final design should communicate a trustworthiness and professionalism.

I have attached photos of a website that I really think is great, so if we could have something that follows along those likes,

https://www.dailyplover.example/local-news/news/local-builder-named-top-apprentice-for-region/QZTRPLA8VXN2MJ5DFYUEKHSWGO/

I won a competition a few years ago while I was an apprentice, If we could somehow put that in there as one of my achievements to try to bring in some trust that would be awesome. I would like to add a new picture though because my beard in that photo is wild.

Target Market(s)

Families that want live in the homes that i'm working on. not investors. People that are looking for quality not cheapest price.

Industry/Entity Type

Construction, Home renovations, Maintenance, Deck Builds, New Builds, Bathrooms, Kitchens

Coding

Coded - Design and coding required

Number of Pages Required

5+ page

Font styles to use
Sans Serif

Colors
6B429C
8869AF
B7A5CE
E3DAEB
F3F0F8

Requirements
Must have
• Contact us page, large clear pictures, Colours the work with the purple in my logo. That will be my company colour so I'm thinking black and purple, or what ever compliments purple nicely
Nice to have
• Page for Renovations, Testimonials, Contact us, Home, About us
Should not have
• Plain looking pages, empty white space, I want the text to be beside a nice big picture etc

```html
<!DOCTYPE html>
<html lang="en">
<head>
<meta charset="utf-8">
<title>Tallow Crest Joinery Ltd — Renovation &amp; Remodeling, Hamilton</title>
<link href="https://fonts.googleapis.com/css2?family=Poppins:wght@300;400;500;600;700&family=Michroma&display=swap" rel="stylesheet">
<style>
:root{
  --purple:#6b429c;
  --purple-mid:#8869af;
  --purple-soft:#b7a5ce;
  --purple-pale:#e3daeb;
  --dark:#3e3d40;
  --darker:#2f2e31;
  --grey-bg:#f4f4f4;
  --card-bg:#f2f2f2;
  --text:#333;
  --muted:#666;
  --white:#fff;
}
*{box-sizing:border-box;margin:0;padding:0}
html,body{width:1200px;height:4764px;overflow:hidden}
body{position:relative;font-family:'Poppins',sans-serif;color:var(--text);background:var(--white)}
.abs{position:absolute}
.btn{position:absolute;display:flex;align-items:center;justify-content:center;font-size:10px;font-weight:600;text-transform:uppercase;color:var(--white);letter-spacing:.3px;white-space:nowrap}
.btn-purple{background:var(--purple)}
.btn-dark{background:var(--dark)}
.brand{display:flex;align-items:center;gap:8px;font-weight:600;color:var(--purple);font-size:15px;line-height:1.15}
.brand i{width:18px;height:18px;background:var(--purple);flex:none}
.section-title{position:absolute;left:0;width:1200px;text-align:center;font-size:29px;font-weight:400;color:var(--dark);letter-spacing:.3px}
.section-title b{font-weight:600}
.section-title .p{color:var(--purple)}
.lead{position:absolute;left:240px;width:720px;text-align:center;font-size:13.5px;line-height:25px;color:var(--text)}

/* header */
.site-header{position:absolute;left:0;top:0;width:1200px;height:115px;background:var(--white)}
.site-header .brand{position:absolute;left:146px;top:36px;width:150px}
.nav a{position:absolute;top:67px;font-size:12px;color:#444;text-decoration:none;text-transform:uppercase;white-space:nowrap}
.nav a.active{color:var(--purple)}
.phone-pill{position:absolute;left:922px;top:15px;width:134px;height:34px;background:var(--dark);color:#fff;font-size:11.5px;display:flex;align-items:center;white-space:nowrap}
.phone-pill span.ic{width:34px;height:34px;background:var(--purple);display:flex;align-items:center;justify-content:center;margin-right:10px}

/* hero */
.hero{position:absolute;left:0;top:115px;width:1200px;height:495px;background:var(--dark)}
.hero-photo{position:absolute;left:0;top:0;width:760px;height:495px;background:linear-gradient(100deg,#8b6a4a 0%,#b99370 35%,#7a6a5c 62%,rgba(62,61,64,0) 100%)}
.hero-title{position:absolute;left:610px;top:148px;font-family:'Michroma',sans-serif;font-size:44px;font-weight:400;color:#fff;line-height:1;white-space:nowrap}
.hero-sub{position:absolute;left:610px;top:218px;font-size:30px;letter-spacing:8px;color:#fff;font-weight:400;white-space:nowrap;line-height:1.2}
.hero-text{position:absolute;left:610px;top:267px;width:440px;font-size:16px;line-height:24px;color:#ddd}

/* feature band */
.feature-band{position:absolute;left:0;top:610px;width:1200px;height:109px}
.feature{position:absolute;top:31px;color:#fff;white-space:nowrap}
.feature h3{font-size:17px;font-weight:600}
.feature p{font-size:14.5px;font-weight:300;color:#ddd;margin-top:4px}

/* about */
.about{position:absolute;left:0;top:719px;width:1200px;height:507px;background:var(--grey-bg)}
.tag{position:absolute;left:146px;top:108px;width:337px;height:27px;background:var(--purple);color:#fff;font-size:14px;font-weight:500;display:flex;align-items:center;justify-content:center;letter-spacing:.3px}
.about h2{position:absolute;left:146px;top:158px;font-size:30px;font-weight:500;color:var(--dark)}
.about p{position:absolute;left:146px;top:207px;width:460px;font-size:13.5px;line-height:25px}
.about-photo{position:absolute;left:667px;top:102px;width:387px;height:314px;background:linear-gradient(135deg,#5a3526 0%,#9a5b3a 45%,#3a2a24 100%)}

/* renovations */
.card{position:absolute;top:1459px;height:359px;background:var(--card-bg)}
.card .photo{height:190px}
.card h3{text-align:center;font-size:18px;font-weight:500;color:var(--purple);margin-top:20px}
.card p{text-align:center;font-size:11.5px;line-height:19px;color:#444;margin:6px 38px 0}
.card .btn{left:50%;transform:translateX(-50%);bottom:-12px;width:100px;height:26px;font-size:9px}
.dot{position:absolute;top:1904px;width:28px;height:28px;border-radius:50%;display:flex;align-items:center;justify-content:center}

/* projects */
.projects{position:absolute;left:0;top:2006px;width:1200px;height:259px;background:var(--grey-bg)}
.strip{position:absolute;top:2265px;height:198px;width:300px}
.strip .btn{top:90px;height:28px;font-size:9px}
.initiatives{position:absolute;left:0;top:2463px;width:1200px;height:98px;background:var(--purple)}

/* tabs */
.tab{position:absolute;top:2609px;width:202px;height:120px;background:var(--card-bg);display:flex;flex-direction:column;align-items:center;justify-content:center;gap:8px;font-size:18px;color:var(--purple)}
.tab.active{background:var(--dark);color:#fff}

/* who */
.who h2{position:absolute;left:331px;top:3030px;font-size:30px;font-weight:600;color:#fff}
.who p{position:absolute;left:331px;width:520px;font-size:13.5px;line-height:25px;color:#fff}

/* testimonials */
.tcard{position:absolute;background:#fff;box-shadow:0 2px 10px rgba(0,0,0,.1);padding:62px 20px 0}
.tcard .av{position:absolute;top:-22px;left:20px;width:60px;height:60px;border-radius:50%;background:linear-gradient(#c9b9a8,#7b6d60)}
.tcard h4{font-size:15px;font-weight:500;color:var(--purple)}
.tcard .role{font-size:10.5px;color:#666;display:flex;justify-content:space-between;margin-top:4px}
.tcard .stars{color:#f2b233;letter-spacing:2px;font-size:10px}
.tcard .q{color:var(--purple);font-size:22px;font-weight:700;margin-top:10px;line-height:1;height:14px}
.tcard p{font-size:8.5px;line-height:15px;color:#777;margin-top:4px}

/* contact */
.contact-side{position:absolute;left:0;top:4031px;width:410px;height:388px;background:var(--grey-bg)}
.c-item{position:absolute;left:168px;font-size:14px;color:var(--purple)}
.c-item small{display:block;font-size:10px;color:#888;line-height:15px;margin-top:2px}
.field{position:absolute;border-bottom:1px solid #999;font-size:10px;color:#444;padding-bottom:6px}

/* footer */
.footer{position:absolute;left:0;top:4419px;width:1200px;height:345px;background:var(--dark);color:#fff}
.fcol{position:absolute;top:76px}
.fcol h4{font-size:16px;font-weight:600}
.fcol a,.fcol div.l{display:block;font-size:10px;color:#eee;text-decoration:none;margin-top:9px}
.social{display:inline-block;width:19px;height:19px;border-radius:50%;border:1px solid #ccc;margin-right:6px}
</style>
</head>
<body>

<header class="site-header">
  <div class="brand"><i></i><span>Tallow Crest<br>Joinery Ltd</span></div>
  <nav class="nav">
    <a class="active" style="left:483px">Home</a>
    <a style="left:575px">About Us</a>
    <a style="left:692px">Renovations</a>
    <a style="left:838px">Testimonials</a>
    <a style="left:978px">Contact Us</a>
  </nav>
  <div class="phone-pill"><span class="ic"><svg width="14" height="14" viewBox="0 0 24 24" fill="none" stroke="#fff" stroke-width="2"><path d="M5 3h4l2 5-3 2a11 11 0 0 0 6 6l2-3 5 2v4a2 2 0 0 1-2 2A17 17 0 0 1 3 5a2 2 0 0 1 2-2z"/></svg></span>021-555-0147</div>
</header>

<section class="hero">
  <div class="hero-photo" role="img" aria-label="Carpenter's hands working with a hammer and drill bits on a timber frame"></div>
  <h1 class="hero-title">TALLOW CREST</h1>
  <div class="hero-sub">JOINERY LTD</div>
  <p class="hero-text">Renovation/Remodeling Company Based In Hamilton, New Zealand</p>
  <a class="btn btn-purple" style="left:610px;top:345px;width:120px;height:32px;font-size:11px">Read More</a>
</section>

<section class="feature-band">
  <svg class="abs" style="left:0;top:0" width="1200" height="109"><rect width="1200" height="109" fill="#3e3d40"/><polygon points="632,0 1200,0 1200,109 567,109" fill="#6b429c"/></svg>
  <svg class="abs" style="left:146px;top:31px" width="40" height="44" viewBox="0 0 40 44" fill="none" stroke="#fff" stroke-width="2"><path d="M20 2 36 8v14c0 10-7 17-16 20C11 39 4 32 4 22V8z"/><path d="m12 22 6 6 11-12"/></svg>
  <div class="feature" style="left:203px"><h3>BEST QUALITY</h3><p>Lorem Ipsum Dolor Sit Amet</p></div>
  <a class="btn btn-purple" style="left:460px;top:41px;width:89px;height:31px;font-size:9px">Get A Quote</a>
  <svg class="abs" style="left:640px;top:33px" width="44" height="40" viewBox="0 0 44 40" fill="none" stroke="#fff" stroke-width="2"><rect x="2" y="2" width="40" height="28" rx="2"/><path d="M10 30 8 38l10-8"/><path d="M26 12h10M26 18h10M26 24h6"/><text x="10" y="23" fill="#fff" stroke="none" font-size="16" font-family="Poppins">$</text></svg>
  <div class="feature" style="left:703px"><h3>QUOTE REQUEST</h3><p>Renovation And Remodeling</p></div>
  <a class="btn btn-dark" style="left:965px;top:41px;width:89px;height:31px;font-size:9px">Get A Quote</a>
</section>

<section class="about">
  <div class="tag">Renovation and Remodeling Solutions</div>
  <h2>About Tallow Crest</h2>
  <p>Lorem Ipsum is simply dummy text of the printing and typesetting industry. Lorem Ipsum has been the industry's standard dummy text ever since the 1500s, when an unknown printer took a galley of type and scrambled it to make a type specimen book. It has survived not only five centuries</p>
  <a class="btn btn-purple" style="left:146px;top:370px;width:92px;height:31px">Learn More</a>
  <div class="about-photo" role="img" aria-label="Smiling tradesman in a hard hat standing in a workshop"></div>
</section>

<section class="renovations">
  <h2 class="section-title" style="top:1308px"><span class="p">OUR</span> <b>RENOVATIONS</b></h2>
  <p class="lead" style="top:1362px">Lorem Ipsum is simply dummy text of the printing and typesetting industry. Lorem Ipsum has been the industry's standard dummy text ever since the 1500s, when an unknown.</p>
  <article class="card" style="left:146px;width:290px">
    <div class="photo" role="img" aria-label="Plumber fitting a bathroom basin" style="background:linear-gradient(135deg,#8a7a6a,#5b6f86)"></div>
    <h3>BATHROOMS</h3><p>Lorem ipsum is simply dummy text of the printing and typesetting industry. Lorem Ipsum.</p>
    <a class="btn btn-dark">Service Detail</a>
  </article>
  <article class="card" style="left:455px;width:292px">
    <div class="photo" role="img" aria-label="Modern kitchen with light timber cabinets" style="background:linear-gradient(135deg,#d8c3a5,#e9e2d8 60%,#9a8c7c)"></div>
    <h3>KITCHEN</h3><p>Lorem ipsum is simply dummy text of the printing and typesetting industry. Lorem Ipsum.</p>
    <a class="btn btn-dark">Service Detail</a>
  </article>
  <article class="card" style="left:765px;width:291px">
    <div class="photo" role="img" aria-label="Gloved hands hammering new deck boards" style="background:linear-gradient(135deg,#3a3230,#c69a62 55%,#e0b983)"></div>
    <h3>DECK BUILDS</h3><p>Lorem ipsum is simply dummy text of the printing and typesetting industry. Lorem Ipsum.</p>
    <a class="btn btn-dark">Service Detail</a>
  </article>
  <span class="dot" style="left:565px;background:var(--dark)"><svg width="10" height="10" viewBox="0 0 10 10"><path d="M7 1 3 5l4 4" stroke="#fff" stroke-width="2" fill="none"/></svg></span>
  <span class="dot" style="left:607px;background:var(--purple)"><svg width="10" height="10" viewBox="0 0 10 10"><path d="m3 1 4 4-4 4" stroke="#fff" stroke-width="2" fill="none"/></svg></span>
</section>

<section class="projects">
  <h2 class="section-title" style="top:84px">RECENT <b class="p">PROJECTS</b></h2>
  <p class="lead" style="top:134px">Lorem Ipsum is simply dummy text of the printing and typesetting industry. Lorem Ipsum has been the industry's standard dummy text ever since the 1500s, when an unknown.</p>
</section>
<div class="strip" style="left:0;background:linear-gradient(135deg,#c9c2b8,#7d7166)" role="img" aria-label="Worker renovating a bright interior room"><a class="btn btn-purple" style="left:98px;width:104px">View Projects</a></div>
<div class="strip" style="left:300px;background:linear-gradient(135deg,#1e1a18,#6b4a32 60%,#2a2220)" role="img" aria-label="Sawdust flying from a power saw cutting timber"></div>
<div class="strip" style="left:600px;background:linear-gradient(135deg,#7a5233,#c08a58 55%,#6a4a32)" role="img" aria-label="Close-up of timber planks being cut"><a class="btn" style="left:98px;width:104px;border:1px solid #fff">View Projects</a></div>
<div class="strip" style="left:900px;background:linear-gradient(135deg,#a89684,#6d5f52)" role="img" aria-label="Builder measuring and marking timber"><a class="btn" style="left:98px;width:104px;border:1px solid #fff">View Projects</a></div>
<section class="initiatives">
  <div class="abs" style="left:397px;top:38px;color:#fff;font-size:16px;font-weight:600;white-space:nowrap">DISCOVER OUR INITIATIVES</div>
  <a class="btn btn-dark" style="left:677px;top:35px;width:127px;height:28px;font-size:9px">View All Projects</a>
</section>

<section class="offer">
  <div class="tab active" style="left:281px">
    <svg width="30" height="28" viewBox="0 0 30 28" fill="none" stroke="#fff" stroke-width="1.6"><rect x="5" y="2" width="20" height="16" rx="1"/><path d="M2 18h26v6H2zM10 8h10M10 12h6"/></svg>We Offer
    <svg class="abs" style="left:91px;bottom:-10px" width="20" height="10"><polygon points="0,0 20,0 10,10" fill="#3e3d40"/></svg>
  </div>
  <div class="tab" style="left:501px">
    <svg width="28" height="30" viewBox="0 0 28 30" fill="none" stroke="#3e3d40" stroke-width="1.6"><path d="M14 2 25 6v9c0 7-5 11-11 13C8 26 3 22 3 15V6z"/><path d="m9 15 4 4 7-8"/></svg>We Guarantee
  </div>
  <div class="tab" style="left:719px">
    <svg width="40" height="28" viewBox="0 0 40 28" fill="none" stroke="#3e3d40" stroke-width="1.6"><rect x="2" y="4" width="22" height="16"/><path d="M24 10h8l5 6v4H24z"/><circle cx="10" cy="22" r="3"/><circle cx="30" cy="22" r="3"/></svg>We Provide
  </div>
  <h2 class="section-title" style="top:2794px;font-size:18px"><span>OUR</span> <b class="p">OFFER</b></h2>
  <p class="lead" style="top:2830px">Lorem Ipsum is simply dummy text of the printing and typesetting industry. Lorem Ipsum has been the industry's standard dummy text ever since the 1500s, when an unknown.</p>
</section>

<section class="who">
  <svg class="abs" style="left:0;top:2973px" width="1200" height="383"><polygon points="0,0 1180,0 1180,383 325,383" fill="#3e3d40"/></svg>
  <div class="brand abs" style="left:50px;top:3230px"><i></i><span>Tallow Crest<br>Joinery Ltd</span></div>
  <h2>Who We Are</h2>
  <p style="top:3083px">Lorem Ipsum is simply dummy text of the printing and typesetting industry. Lorem Ipsum has been the industry's standard dummy text ever since the 1500s, when an unknown.</p>
  <p style="top:3170px">Lorem Ipsum is simply dummy text of the printing and typesetting industry. Lorem Ipsum has been the industry's standard dummy text ever.</p>
  <a class="btn btn-purple" style="left:335px;top:3258px;width:103px;height:26px;font-size:9px;text-transform:none">View More</a>
  <div class="abs" style="left:939px;top:2921px;width:183px;height:183px;border-radius:50%;background:var(--purple)"></div>
  <div class="abs" role="img" aria-label="Bearded tradesman in overalls standing with arms crossed" style="left:887px;top:3010px;width:287px;height:346px;border-radius:140px 140px 0 0;background:linear-gradient(#b9a592,#8d8d8f 45%,#5a5a5c)"></div>
</section>

<section class="testimonials">
  <h2 class="section-title" style="top:3465px"><span>OUR</span> <b class="p">TESTIMONIALS</b></h2>
  <p class="lead" style="top:3514px">Lorem Ipsum is simply dummy text of the printing and typesetting industry. Lorem Ipsum has been the industry's standard dummy text ever since the 1500s, when an unknown.</p>

  <article class="tcard" style="left:-38px;top:3633px;width:226px;height:223px;opacity:.55">
    <div class="av" role="img" aria-label="Customer portrait"></div><h4>Helen T.</h4><div class="role">Homeowner<span class="stars">★★★★★</span></div><div class="q">“</div><p>Our new deck was built on time and on budget. Clear updates every week and spotless tidy-up at the end. We would happily recommend this team.</p>
  </article>
  <article class="tcard" style="left:226px;top:3680px;width:225px;height:222px">
    <div class="av" role="img" aria-label="Customer portrait"></div><h4>Helen T.</h4><div class="role">Homeowner<span class="stars">★★★★★</span></div><div class="q">“</div><p>Our new deck was built on time and on budget. Clear updates every week and spotless tidy-up at the end. We would happily recommend this team.</p>
  </article>
  <article class="tcard" style="left:486px;top:3680px;width:228px;height:222px">
    <div class="av" role="img" aria-label="Customer portrait"></div><h4>Aaron K.</h4><div class="role">Homeowner<span class="stars">★★★★★</span></div><div class="q">“</div><p>The kitchen renovation turned out better than we imagined. Careful work, honest advice and great finishing on every joint and cabinet door.</p>
  </article>
  <article class="tcard" style="left:751px;top:3680px;width:227px;height:222px">
    <div class="av" role="img" aria-label="Customer portrait"></div><h4>Rangi P.</h4><div class="role">Homeowner<span class="stars">★★★★★</span></div><div class="q">“</div><p>Friendly, reliable and skilled. Our bathroom now feels brand new and the whole job ran smoothly from the first quote to the final clean.</p>
  </article>
  <article class="tcard" style="left:1011px;top:3633px;width:226px;height:223px;opacity:.55">
    <div class="av" role="img" aria-label="Customer portrait"></div><h4>Helen T.</h4><div class="role">Homeowner<span class="stars">★★★★★</span></div><div class="q">“</div><p>Our new deck was built on time and on budget. Clear updates every week and spotless tidy-up at the end. We would happily recommend this team.</p>
  </article>
  <svg class="abs" style="left:558px;top:3940px" width="90" height="12"><path d="M2 6h22M2 6l5-4M2 6l5 4" stroke="#6b429c" stroke-width="1.5" fill="none"/><path d="M50 6h36M86 6l-5-4M86 6l-5 4" stroke="#333" stroke-width="1.5" fill="none"/></svg>
</section>

<section class="contact">
  <div class="contact-side">
    <div class="brand abs" style="left:146px;top:80px"><i></i><span>Tallow Crest<br>Joinery Ltd</span></div>
  </div>
  <svg class="abs" style="left:144px;top:4237px" width="12" height="16" viewBox="0 0 12 16" fill="none" stroke="#6b429c" stroke-width="1.5"><path d="M6 15S1 9 1 6a5 5 0 0 1 10 0c0 3-5 9-5 9z"/><circle cx="6" cy="6" r="2"/></svg>
  <div class="c-item" style="top:4234px">Location<small>12 Kowhai Lane,<br>Hamilton 3204</small></div>
  <svg class="abs" style="left:144px;top:4307px" width="14" height="14" viewBox="0 0 24 24" fill="none" stroke="#6b429c" stroke-width="2"><path d="M5 3h4l2 5-3 2a11 11 0 0 0 6 6l2-3 5 2v4a2 2 0 0 1-2 2A17 17 0 0 1 3 5a2 2 0 0 1 2-2z"/></svg>
  <div class="c-item" style="top:4304px">Contact Us<small>021-555-0198</small></div>

  <h3 class="abs" style="left:466px;top:4085px;font-size:17px;font-weight:600;letter-spacing:2.5px;color:var(--purple);white-space:nowrap">FOR ANY QUESTIONS SEND US A MESSAGE</h3>
  <div class="field" style="left:466px;top:4139px;width:283px">First Name*</div>
  <div class="field" style="left:466px;top:4195px;width:283px">Last Name*</div>
  <div class="field" style="left:466px;top:4253px;width:283px">Email Address</div>
  <div class="abs" style="left:773px;top:4139px;font-size:10px;color:#444">Your Message</div>
  <div class="abs" style="left:773px;top:4273px;width:283px;border-bottom:1px solid #999"></div>
  <a class="btn btn-dark" style="left:928px;top:4321px;width:128px;height:33px;font-size:11px">Submit</a>
</section>

<footer class="footer">
  <div class="abs" style="left:137px;top:67px;width:153px;height:118px;background:#fff;display:flex;align-items:center;justify-content:center"><div class="brand"><i></i><span>Tallow Crest<br>Joinery Ltd</span></div></div>
  <div class="fcol" style="left:379px"><h4>Our Company</h4><a>Home</a><a>About Us</a><a>Renovations</a><a>Testimonials</a><a>Contact Us</a></div>
  <div class="fcol" style="left:592px"><h4>Partner With Us</h4><a>Privacy Policies</a><a>Term and Conditions</a><a>Term and Services</a></div>
  <div class="fcol" style="left:823px"><h4>Contact Us</h4>
    <div class="l">✉&nbsp; hello@tallowcrest.example</div>
    <div class="l">⌖&nbsp; Hamilton 3204</div>
    <div style="margin-top:12px"><span class="social" style="background:var(--purple);border-color:var(--purple)"></span><span class="social"></span><span class="social"></span></div>
  </div>
  <div class="abs" style="left:0;width:1200px;top:306px;text-align:center;font-size:10px;color:#ddd">Copyright © 2023 tallowcrest.example. All rights Reserved.</div>
</footer>

</body>
</html>
```